Hackthon event need a Landing Page

We are looking for a landing page to represent an event we are preparing in our country (Dominican Republic), it would be the first of this type, and we want to create a positive impact and make it a brand to make it recurring year to year .

The event is a hackathon where we will be gathering students and professionals to solve challenges using software development.

This landing page should be resposive, multi-language, clean, modern and align with the event logo.

Find a good example of what we are looking for in the following link:

https://brightcodefest.example/

We would like to have the following sections(Not necesarily in this order, not necesarily all of them):

- Brief
- Agenda
- Countdown
- Form Button to redirect to the event registration service.
---> Note: We would like to see the option of having the form in the landing page.
- Contact info and Social Media
- Partners/Sponsors
- Link to intro video

We will be attaching the logo and the variations of colors we are looking to see. It should be with a black background

```html
<!DOCTYPE html>
<html lang="en">
<head>
<meta charset="utf-8">
<title>CodeFiesta — Hackathon Landing Page</title>
<link rel="stylesheet" href="https://fonts.googleapis.com/css2?family=Audiowide&family=Poppins:wght@400;500;600;700&display=swap">
<style>
  :root{
    --green:#4fd41d;
    --green-dim:#3a9e16;
    --bg:#1c1c1c;
    --bg-deep:#0d0d0d;
    --panel:#0a0a0a;
    --box:#111111;
    --text:#ffffff;
    --muted:#d4d4d4;
    --field:#ffffff;
    --display:"Audiowide", sans-serif;
    --body:"Poppins", sans-serif;
  }
  *{box-sizing:border-box;margin:0;padding:0}
  html,body{width:1200px;height:5186px;overflow:hidden;background:var(--bg);color:var(--text);font-family:var(--body)}
  .page{position:relative;width:1200px;height:5186px;overflow:hidden}
  .abs{position:absolute}

  /* shared */
  .btn{position:absolute;display:flex;align-items:center;justify-content:center;color:var(--green);font-size:14px;letter-spacing:.5px;font-family:var(--body)}
  .btn::before{content:"";position:absolute;inset:0;border:2px solid var(--green);transform:skewX(-28deg)}
  .section-title{position:absolute;left:0;width:1200px;text-align:center;font-family:var(--display);font-size:27px;letter-spacing:3px;text-transform:uppercase}
  .brand{font-family:var(--body);font-weight:700;color:var(--green);display:flex;align-items:center;gap:8px}
  .brand .dot{width:14px;height:14px;border-radius:50%;background:var(--green)}

  /* header + hero */
  .hero-bg{left:0;top:0;width:1200px;height:860px;background:linear-gradient(180deg,#141414 0%,#1a1a1a 100%)}
  .hero-photo{left:560px;top:0;width:640px;height:640px;background:radial-gradient(ellipse at 70% 35%,#3b4450 0%,#1e242b 40%,#141414 75%)}
  .header-brand{left:86px;top:62px;font-size:22px}
  .menu{left:994px;top:34px;width:28px}
  .menu span{display:block;height:3px;background:#fff;margin-bottom:7px;border-radius:2px}
  .menu span:nth-child(2){width:22px}
  .lang{left:1053px;top:24px;width:91px;height:42px;border:2px solid #fff;border-radius:21px;display:flex;align-items:center;justify-content:center;gap:8px;font-size:14px}
  .lang .globe{width:24px;height:24px;border-radius:50%;background:#b02030;border:2px solid #fff}
  .hero-kicker{left:156px;top:244px;font-size:42px;font-weight:500;letter-spacing:1px}
  .hero-title{left:154px;top:286px;font-size:74px;font-weight:700;line-height:1}
  .hero-text{left:158px;top:378px;width:500px;font-size:18px;line-height:41px;color:var(--muted)}
  .hero-line{left:0;top:600px}
  .event-box{left:694px;top:600px;width:423px;height:256px;background:var(--panel);border:4px solid var(--green);padding:30px 0 0 50px}
  .event-date{font-family:var(--display);color:var(--green);font-size:22px;letter-spacing:1px}
  .event-lines{margin-top:22px;font-family:var(--display);font-size:21px;line-height:40.5px;letter-spacing:1px;text-transform:uppercase}

  /* feature cards */
  .card{top:930px;width:256px;height:400px;background:var(--box);border-top:4px solid var(--green);border-left:4px solid var(--green);text-align:center;padding-top:30px}
  .card::after{content:"";position:absolute;right:-6px;top:-4px;width:6px;height:120px;background:#1c1c1c}
  .card-icon{width:64px;height:64px;margin:0 auto}
  .card h3{margin-top:22px;font-size:15px;font-weight:600;color:var(--green);letter-spacing:.3px}
  .card p{margin:26px auto 0;width:200px;font-size:12.5px;line-height:30px;color:var(--muted)}
  .card .more{display:block;margin-top:14px;font-size:14px;font-weight:600;color:var(--green)}
  .how-title{left:735px;top:966px;font-family:var(--display);font-size:27px;letter-spacing:3px}
  .how-text{left:735px;top:1020px;width:330px;font-size:15.5px;line-height:30.2px;color:var(--muted)}

  /* agenda */
  .agenda-bg{left:0;top:1425px;width:1200px;height:910px;background:#151515;border-top:6px solid var(--green);border-bottom:6px solid var(--green)}
  .agenda-panel{left:97px;top:1506px;width:1026px;height:729px;background:radial-gradient(ellipse at 50% 75%,#173a12 0%,#0b120a 45%,#070707 80%)}
  .agenda-title{top:1544px}
  .day{width:252px;height:252px;background:rgba(6,6,6,.92)}
  .day h4{text-align:center;font-family:var(--display);font-size:20px;color:var(--green);letter-spacing:1px;margin-top:16px;font-weight:400}
  .day table{margin:20px 0 0 10px;border-collapse:collapse;font-size:17px}
  .day td{height:29px;padding:0}
  .day td:first-child{width:112px}
  .circuit{left:0;top:1420px}

  /* countdown */
  .count-panel{left:100px;top:2405px;width:1013px;height:403px;background:linear-gradient(90deg,#0c1a0a 0%,#0a0f0a 35%,#101a0e 100%);border:4px solid var(--green);box-shadow:0 0 22px rgba(79,212,29,.45)}
  .count-art{left:104px;top:2409px;width:330px;height:395px;background:radial-gradient(ellipse at 40% 45%,#1f3d18 0%,#0d1a0b 60%,transparent 100%)}
  .only{left:296px;top:2500px;font-family:var(--display);font-size:40px;letter-spacing:3px}
  .big-three{left:446px;top:2430px;font-family:var(--display);font-size:240px;line-height:1;color:#fff;text-shadow:0 0 0 var(--green),4px 4px 0 var(--green),-3px -3px 0 var(--green)}
  .timer{left:650px;top:2508px;font-family:var(--display);font-size:27px;letter-spacing:4px;line-height:46px}
  .timer .sub{font-size:20px;color:var(--green);letter-spacing:1px}

  /* video */
  .video-section{left:0;top:2865px;width:1200px;height:720px;background:linear-gradient(180deg,#141414 0%,#0c0c0c 60%,#1a1a1a 100%)}
  .video-title{top:2908px}
  .video-text{left:0;top:2953px;width:1200px;text-align:center;font-size:16px;line-height:30px;color:var(--muted)}
  .video-frame{left:129px;top:3054px;width:952px;height:463px;background:linear-gradient(120deg,#1d2a33 0%,#3c4650 40%,#5a5652 65%,#2a2c30 100%)}
  .play{left:574px;top:3253px;width:64px;height:64px;border-radius:50%;background:#fff;border:5px solid var(--green);display:flex;align-items:center;justify-content:center}
  .expand{left:1020px;top:3072px}

  /* partners */
  .partners-title{top:3615px}
  .partner{top:3700px;width:254px;height:121px;background:#202020;border:4px solid var(--green);box-shadow:0 0 14px rgba(79,212,29,.5);display:flex;align-items:center;justify-content:center}
  .partner .mark{width:150px;height:34px;border-radius:6px;background:#3d3d3d}

  /* registration */
  .reg-title{top:3954px}
  .reg-text{left:160px;top:4013px;width:880px;text-align:center;font-size:16px;line-height:30px;color:var(--muted)}

  /* contact */
  .contact-panel{left:80px;top:4278px;width:1017px;height:489px;background:radial-gradient(ellipse at 70% 60%,#12260f 0%,#080808 55%,#050505 100%)}
  .contact-title{top:4340px}
  .field{position:absolute;height:58px;background:var(--field);color:#555;font-size:15px;padding-left:32px;display:flex;align-items:center}

  /* footer */
  .footer-wedge{left:0;top:4800px}
  .footer-brand{left:0;top:4912px;width:1200px;justify-content:center;font-size:26px}
  .contact-item{top:5030px;display:flex;align-items:center;gap:12px;font-size:16px;color:var(--muted)}
  .copyright{left:111px;top:5118px;font-size:16px;color:var(--muted)}
  .social{top:5107px;display:flex;align-items:center;gap:8px;font-size:13px;color:var(--muted)}
  .social .ring{width:14px;height:14px;border-radius:50%;border:2px solid #fff}
</style>
</head>
<body>
<div class="page">

  <!-- HERO -->
  <div class="abs hero-bg"></div>
  <div class="abs hero-photo" role="img" aria-label="Programmer in dark light surrounded by floating binary digits"></div>

  <div class="abs brand header-brand"><span class="dot"></span>CodeFiesta</div>
  <div class="abs menu"><span></span><span></span><span></span></div>
  <div class="abs lang"><span class="globe"></span>ENG</div>

  <div class="abs hero-kicker">WELCOME TO</div>
  <h1 class="abs hero-title">CodeFiesta</h1>
  <p class="abs hero-text">Hackathon where we will be gathering students and professionals to solve challenges using software development</p>
  <div class="btn" style="left:152px;top:523px;width:160px;height:38px">REGISTER NOW</div>

  <svg class="abs hero-line" width="1200" height="260" viewBox="0 600 1200 260">
    <polyline points="0,668 594,800 1200,690" fill="none" stroke="var(--green)" stroke-width="12"/>
  </svg>

  <div class="abs event-box">
    <div class="event-date">October 25 - 28, 2022</div>
    <div class="event-lines">Worldwide - Online<br>&amp;<br>America vs<br>Russia Towers Fight</div>
  </div>

  <!-- FEATURES -->
  <article class="abs card" style="left:90px">
    <svg class="card-icon" viewBox="0 0 64 64"><circle cx="32" cy="32" r="29" fill="none" stroke="var(--green)" stroke-width="3"/><circle cx="32" cy="24" r="6" fill="var(--green)"/><circle cx="20" cy="30" r="5" fill="var(--green)"/><circle cx="44" cy="30" r="5" fill="var(--green)"/><path d="M22 46a10 10 0 0 1 20 0z" fill="var(--green)"/></svg>
    <h3>STRATEGIZE &amp; EXECUTE</h3>
    <p>Lorem Ipsum is simply dummy text of the printing and typesetting industry. Lorem Ipsum has been the industry's standard dummy text ever since the 1500s,</p>
    <span class="more">READ MORE</span>
  </article>
  <article class="abs card" style="left:413px">
    <svg class="card-icon" viewBox="0 0 64 64"><g fill="var(--green)"><rect x="8" y="44" width="8" height="14"/><rect x="20" y="36" width="8" height="22"/><rect x="32" y="28" width="8" height="30"/><rect x="44" y="20" width="8" height="38"/></g><polyline points="6,38 22,26 34,30 54,8" fill="none" stroke="var(--green)" stroke-width="3"/><polygon points="56,4 56,14 46,6" fill="var(--green)"/></svg>
    <h3>GROW &amp; MAINTAIN</h3>
    <p>Lorem Ipsum is simply dummy text of the printing and typesetting industry. Lorem Ipsum has been the industry's standard dummy text ever since the 1500s,</p>
    <span class="more">READ MORE</span>
  </article>

  <h2 class="abs how-title">HOW WE WORKS ?</h2>
  <p class="abs how-text">Lorem Ipsum is simply dummy text of the printing and typesetting industry. Lorem Ipsum has been the industry's standard dummy text ever since the 1500s, when an unknown printer took a galley of type and scrambled it to make a type specimen book. It has survived not only five centuries, but also the leap into electronic.</p>

  <!-- AGENDA -->
  <div class="abs agenda-bg"></div>
  <div class="abs agenda-panel" role="img" aria-label="Dark green glowing network backdrop"></div>
  <svg class="abs circuit" width="1200" height="840" viewBox="0 1420 1200 840" fill="none" stroke="var(--green)" stroke-width="3">
    <polyline points="0,1540 207,1540 207,1584"/><circle cx="207" cy="1586" r="8" fill="var(--green)"/>
    <polyline points="860,1431 860,1468 764,1468 764,1582"/><circle cx="764" cy="1586" r="8" fill="var(--green)"/>
    <line x1="1070" y1="1893" x2="1200" y2="1893"/><circle cx="1070" cy="1893" r="8" fill="var(--green)"/>
    <line x1="0" y1="2008" x2="155" y2="2008"/><circle cx="155" cy="2008" r="8" fill="var(--green)"/>
    <polyline points="882,2208 882,2256 1200,2256"/><circle cx="882" cy="2208" r="8" fill="var(--green)"/>
  </svg>
  <h2 class="section-title agenda-title">Agenda</h2>

  <section class="abs day" style="left:215px;top:1610px">
    <h4>DAY 1</h4>
    <table><tr><td>2:00-2:30</td><td>Lorem Ipsum</td></tr><tr><td>6:00-7:30</td><td>Registration</td></tr><tr><td>8:00-8:30</td><td>Lorem Ipsum</td></tr><tr><td>5:00-6:30</td><td>Lorem Ipsum</td></tr><tr><td>8:00-9:30</td><td>Registration</td></tr><tr><td>11:00-4:30</td><td>Live Coding</td></tr></table>
  </section>
  <section class="abs day" style="left:497px;top:1604px">
    <h4>DAY 2</h4>
    <table><tr><td>2:00-2:30</td><td>Lorem Ipsum</td></tr><tr><td>6:00-7:30</td><td>Registration</td></tr><tr><td>8:00-8:30</td><td>Lorem Ipsum</td></tr><tr><td>5:00-6:30</td><td>Lorem Ipsum</td></tr><tr><td>8:00-9:30</td><td>Registration</td></tr><tr><td>11:00-4:30</td><td>Live Coding</td></tr></table>
  </section>
  <section class="abs day" style="left:776px;top:1606px">
    <h4>DAY 3</h4>
    <table><tr><td>2:00-2:30</td><td>Lorem Ipsum</td></tr><tr><td>6:00-7:30</td><td>Registration</td></tr><tr><td>8:00-8:30</td><td>Lorem Ipsum</td></tr><tr><td>5:00-6:30</td><td>Lorem Ipsum</td></tr><tr><td>8:00-9:30</td><td>Registration</td></tr><tr><td>11:00-4:30</td><td>Live Coding</td></tr></table>
  </section>
  <section class="abs day" style="left:211px;top:1924px">
    <h4>DAY 4</h4>
    <table><tr><td>2:00-2:30</td><td>Lorem Ipsum</td></tr><tr><td>6:00-7:30</td><td>Registration</td></tr><tr><td>8:00-8:30</td><td>Lorem Ipsum</td></tr><tr><td>5:00-6:30</td><td>Lorem Ipsum</td></tr><tr><td>8:00-9:30</td><td>Registration</td></tr><tr><td>11:00-4:30</td><td>Live Coding</td></tr></table>
  </section>
  <section class="abs day" style="left:493px;top:1918px">
    <h4>DAY 5</h4>
    <table><tr><td>2:00-2:30</td><td>Lorem Ipsum</td></tr><tr><td>6:00-7:30</td><td>Registration</td></tr><tr><td>8:00-8:30</td><td>Lorem Ipsum</td></tr><tr><td>5:00-6:30</td><td>Lorem Ipsum</td></tr><tr><td>8:00-9:30</td><td>Registration</td></tr><tr><td>11:00-4:30</td><td>Live Coding</td></tr></table>
  </section>
  <section class="abs day" style="left:772px;top:1920px">
    <h4>DAY 6</h4>
    <table><tr><td>2:00-2:30</td><td>Lorem Ipsum</td></tr><tr><td>6:00-7:30</td><td>Registration</td></tr><tr><td>8:00-8:30</td><td>Lorem Ipsum</td></tr><tr><td>5:00-6:30</td><td>Lorem Ipsum</td></tr><tr><td>8:00-9:30</td><td>Registration</td></tr><tr><td>11:00-4:30</td><td>Live Coding</td></tr></table>
  </section>

  <!-- COUNTDOWN -->
  <div class="abs count-panel"></div>
  <div class="abs count-art" role="img" aria-label="Green circuit-board silhouette illustration"></div>
  <div class="abs only">ONLY</div>
  <div class="abs big-three">3</div>
  <div class="abs timer">09:12:34<br>DAYS LEFT<br><span class="sub">days until the live stream!</span></div>
  <div class="btn" style="left:513px;top:2706px;width:173px;height:38px">REGISTER NOW</div>

  <!-- VIDEO -->
  <div class="abs video-section"></div>
  <h2 class="section-title video-title">Video</h2>
  <p class="abs video-text">We would love to review your existing website and active marketing<br>campaigns and discuss how we can improve them.</p>
  <div class="abs video-frame" role="img" aria-label="Video still of two people working at computer monitors in an office"></div>
  <div class="abs play"><svg width="22" height="24" viewBox="0 0 22 24"><polygon points="4,2 20,12 4,22" fill="var(--green)"/></svg></div>
  <svg class="abs expand" width="40" height="36" viewBox="0 0 40 36" fill="none" stroke="var(--green)" stroke-width="3"><rect x="2" y="2" width="22" height="18"/><rect x="16" y="14" width="22" height="18"/></svg>

  <!-- PARTNERS -->
  <h2 class="section-title partners-title">Our Partners</h2>
  <div class="abs partner" style="left:44px"><span class="mark"></span></div>
  <div class="abs partner" style="left:326px"><span class="mark"></span></div>
  <div class="abs partner" style="left:608px"><span class="mark"></span></div>
  <div class="abs partner" style="left:890px"><span class="mark" style="width:90px;height:60px;border-radius:50%"></span></div>

  <!-- REGISTRATION -->
  <h2 class="section-title reg-title">Event Registration Service</h2>
  <p class="abs reg-text">Lorem Ipsum is simply dummy text of the printing and typesetting industry. Lorem Ipsum has been the industry's standard dummy text ever since the 1500s, when an unknown printer took a galley of type and scrambled it to make a type specimen book. It has survived not only five centuries, but also the leap into electronic.</p>
  <div class="btn" style="left:507px;top:4173px;width:173px;height:38px">REGISTER NOW</div>

  <!-- CONTACT -->
  <div class="abs contact-panel" role="img" aria-label="Dark backdrop with faint green network glow"></div>
  <h2 class="section-title contact-title">Contact Us</h2>
  <div class="field" style="left:231px;top:4427px;width:369px">First Name</div>
  <div class="field" style="left:618px;top:4427px;width:368px">Last Name</div>
  <div class="field" style="left:231px;top:4509px;width:369px">Email Id</div>
  <div class="field" style="left:618px;top:4509px;width:368px">Phone</div>
  <div class="field" style="left:231px;top:4594px;width:755px">Message</div>
  <div class="btn" style="left:526px;top:4692px;width:173px;height:39px">SUBMIT</div>

  <!-- FOOTER -->
  <svg class="abs footer-wedge" width="1200" height="140" viewBox="0 4800 1200 140">
    <polygon points="70,4932 600,4822 1128,4932 600,4844" fill="var(--green)"/>
  </svg>
  <div class="abs brand footer-brand"><span class="dot"></span>CodeFiesta</div>

  <div class="abs contact-item" style="left:150px">
    <svg width="20" height="24" viewBox="0 0 20 24" fill="none" stroke="#fff" stroke-width="2"><path d="M10 22s8-8 8-13a8 8 0 0 0-16 0c0 5 8 13 8 13z"/><circle cx="10" cy="9" r="3"/></svg>
    27 Fiesta Lane, Santo Domingo.
  </div>
  <div class="abs contact-item" style="left:576px">
    <svg width="22" height="22" viewBox="0 0 22 22" fill="none" stroke="#fff" stroke-width="2"><path d="M4 2h4l2 5-3 2a12 12 0 0 0 6 6l2-3 5 2v4a2 2 0 0 1-2 2A18 18 0 0 1 2 4a2 2 0 0 1 2-2z"/></svg>
    0400 318 275
  </div>
  <div class="abs contact-item" style="left:843px">
    <svg width="26" height="20" viewBox="0 0 26 20" fill="none" stroke="#fff" stroke-width="2"><rect x="1" y="1" width="24" height="18"/><polyline points="1,1 13,11 25,1"/></svg>
    hello@codefiesta.example
  </div>

  <div class="abs copyright">2022 CodeFiesta. All Rights Reserved.</div>
  <div class="abs social" style="left:905px"><span class="ring"></span>Chatterly</div>
  <div class="abs social" style="left:1010px"><span class="ring"></span>Snapline</div>

</div>
</body>
</html>
```